Cedar Hollow Morning Light Minister

Need this banner to stand out, and look like a poster for a movie. The Color scheme, I'm looking for are darker, more dismal doom and gloom? and make it say be heal and be delivered TODAY.

```html
<!DOCTYPE html>
<html lang="en">
<head>
<meta charset="utf-8">
<title>Got Demons? – Cedar Hollow Morning Light Minister banners</title>
<link rel="stylesheet" href="https://fonts.googleapis.com/css2?family=Bebas+Neue&family=Oswald:wght@500;700&display=swap">
<style>
  :root {
    --stage: #3b3b3b;
    --stage-edge: #555555;
    --headline: #f3a43e;
    --title-gold: #f4cb3c;
    --title-white: #f7f3ec;
    --tagline-peach: #f8c9a2;
    --tagline-gold: #f4c63a;
    --url-white: #ffffff;
    --url-gold: #f4c63a;
    --ink-shadow: rgba(0,0,0,0.55);
  }
  * { box-sizing: border-box; margin: 0; padding: 0; }
  html, body {
    width: 718px; height: 1200px; overflow: hidden;
    background: var(--stage);
  }
  .stage {
    position: relative; width: 718px; height: 1200px;
    background: var(--stage);
  }
  .banner {
    position: absolute; top: 7px; width: 328px; height: 1188px;
    overflow: hidden; border: 1px solid var(--stage-edge);
    text-align: center;
  }
  .banner--dawn { left: 8px; }
  .banner--inferno { left: 383px; }

  .banner__art { position: absolute; inset: 0; }
  .banner--dawn .banner__art {
    background:
      radial-gradient(ellipse 40% 55% at 50% 28%, rgba(255,230,245,0.75), rgba(255,180,220,0) 70%),
      linear-gradient(180deg, #4a3a8e 0%, #b05aa8 18%, #e58ab4 32%, #a070c0 46%, #4f4f9c 60%, #2b3f7a 75%, #162033 90%, #0c1018 100%);
  }
  .banner--inferno .banner__art {
    background:
      radial-gradient(ellipse 55% 30% at 50% 22%, rgba(255,190,80,0.7), rgba(255,120,30,0) 70%),
      radial-gradient(ellipse 70% 25% at 50% 85%, rgba(240,90,20,0.75), rgba(200,50,10,0) 70%),
      linear-gradient(180deg, #2a0f0a 0%, #7a2a12 18%, #a8401a 30%, #5a1a0e 48%, #3a0e08 62%, #8a2a10 80%, #2a0906 100%);
  }

  .headline, .ministry-name, .tagline, .web-address {
    position: absolute; left: 0; right: 0; white-space: nowrap;
  }
  .headline {
    top: 38px;
    font-family: "Bebas Neue", sans-serif; font-weight: 400;
    color: var(--headline); font-size: 106px; line-height: 100px;
    text-shadow: 0 3px 6px var(--ink-shadow);
  }
  .headline span { display: block; }

  .ministry-name {
    top: 540px;
    font-family: "Bebas Neue", sans-serif; font-weight: 400;
    text-transform: uppercase;
    text-shadow: 0 3px 8px var(--ink-shadow);
  }
  .banner--dawn .ministry-name { color: var(--title-gold); }
  .banner--inferno .ministry-name { color: var(--title-white); }
  .ministry-name__place { display: block; font-size: 58px; line-height: 60px; }
  .ministry-name__main  { display: block; font-size: 100px; line-height: 104px; }
  .ministry-name__sub   { display: block; font-size: 62px; line-height: 62px; }
  .ministry-name__last  { display: block; font-size: 68px; line-height: 66px; }

  .tagline {
    top: 966px;
    font-family: "Oswald", sans-serif; font-weight: 500;
    text-shadow: 0 2px 5px var(--ink-shadow);
  }
  .banner--dawn .tagline { color: var(--tagline-peach); }
  .banner--inferno .tagline { color: var(--tagline-gold); }
  .tagline__line { display: block; font-size: 31px; line-height: 38px; }
  .tagline__today { display: block; font-size: 58px; line-height: 68px; font-weight: 700; }

  .web-address {
    top: 1134px;
    font-family: "Oswald", sans-serif; font-weight: 500;
    font-size: 28px; line-height: 38px;
    text-shadow: 0 2px 5px var(--ink-shadow);
  }
  .banner--dawn .web-address { color: var(--url-white); }
  .banner--inferno .web-address { color: var(--url-gold); }
</style>
</head>
<body>
<main class="stage">
  <section class="banner banner--dawn">
    <div class="banner__art" role="img" aria-label="Fantasy landscape: a beam of light from glowing pink and purple clouds onto a distant spire, a lone figure walking through a blue valley"></div>
    <h1 class="headline"><span>GOT</span><span>DEMONS?</span></h1>
    <h2 class="ministry-name">
      <span class="ministry-name__place">Cedar Hollow</span>
      <span class="ministry-name__main">Morning</span>
      <span class="ministry-name__sub">Light</span>
      <span class="ministry-name__last">Minister</span>
    </h2>
    <p class="tagline">
      <span class="tagline__line">Be healed, Be delivered</span>
      <span class="tagline__line">Be SET FREE</span>
      <span class="tagline__today">TODAY!</span>
    </p>
    <p class="web-address">cedarhollowministries.com</p>
  </section>

  <section class="banner banner--inferno">
    <div class="banner__art" role="img" aria-label="Dark fiery scene: a burning gothic castle under red smoke with shadowy demonic figures among flames below"></div>
    <h1 class="headline"><span>GOT</span><span>DEMONS?</span></h1>
    <h2 class="ministry-name">
      <span class="ministry-name__place">Cedar Hollow</span>
      <span class="ministry-name__main">Morning</span>
      <span class="ministry-name__sub">Light</span>
      <span class="ministry-name__last">Minister</span>
    </h2>
    <p class="tagline">
      <span class="tagline__line">Be healed, Be delivered</span>
      <span class="tagline__line">Be SET FREE</span>
      <span class="tagline__today">TODAY!</span>
    </p>
    <p class="web-address">cedarhollowministries.com</p>
  </section>
</main>
</body>
</html>
```